K&T Fixit and Rebuild general contracting business card design

I already have a logo that I want to use and I need a card that uses that logo and color scheme on the front with the address phone numbers and email and on the back a place for technicians to write in their name and phone number when they hand it out. It will need the License number of License #KTFXTRB318QN.
It should say General Contractor under the company name. The address is
4417 NE 3rd Ave, Ste D246
Vancouver, WA 98612
www.kandtfixitandrebuild.example
office@kandtfixitandrebuild.example
360-555-0182 is the telephone number
360-555-0149 is the fax number

Target Market(s)

Homeowners needing remodel work or repairs in their home.

Industry/Entity Type

Construction

Contact Information for Business Card

Business name, address, phone number, license number, fax number, email, and website on the front and a place to fill in technician's name and number

Font styles to use
Serif

Requirements
Must have
• Business name, address, phone number, license number, fax number, email, and website on the front and a place to fill in technician's name and number
Nice to have
• I uploaded an example of a front that is good.
Should not have
• Froo froo or extra embellishments.

```html
<!DOCTYPE html>
<html lang="en">
<head>
<meta charset="utf-8">
<title>K&amp;T Fixit and Rebuild — Business Card</title>
<link rel="stylesheet" href="https://fonts.googleapis.com/css2?family=Open+Sans:wght@400;600;700&family=Orbitron:wght@600&display=swap">
<style>
  :root {
    --backdrop: #e3e3e3;
    --card-white: #f4f4f4;
    --wood-light: #a8642f;
    --wood-mid: #7c4420;
    --wood-dark: #4a2712;
    --brand-brown: #a65a2c;
    --band-brown: #7b4320;
    --band-dark: #3d1f0e;
    --ink: #2b2b2b;
    --rule: #6d6d6d;
    --white: #ffffff;
  }
  * { box-sizing: border-box; margin: 0; padding: 0; }
  html, body { width: 1200px; height: 960px; overflow: hidden; }
  body {
    position: relative;
    background: var(--backdrop);
    font-family: "Open Sans", Arial, sans-serif;
    color: var(--ink);
  }
  .card {
    position: absolute;
    left: 310px;
    width: 590px;
    height: 337px;
    border-radius: 18px;
    overflow: hidden;
  }
  /* Front */
  .card--front { top: 127px; }
  .front-artwork {
    position: absolute; inset: 0;
    background:
      radial-gradient(ellipse at 50% 45%, var(--wood-light) 0%, var(--wood-mid) 55%, var(--wood-dark) 100%);
  }
  .front-brand {
    position: absolute; left: 0; right: 0; top: 118px;
    text-align: center; color: var(--white);
  }
  .front-brand__name {
    font-size: 42px; font-weight: 700; letter-spacing: 0.5px; line-height: 1.1;
  }
  .front-brand__tagline {
    margin-top: 38px;
    font-family: "Orbitron", "Open Sans", sans-serif;
    font-weight: 600; font-size: 19px; letter-spacing: 1px;
    text-transform: uppercase;
  }
  /* Back */
  .card--back { top: 516px; background: var(--card-white); }
  .back-brand {
    position: absolute; left: 44px; top: 52px; width: 240px;
    font-size: 36px; font-weight: 700; line-height: 1.12;
    color: var(--brand-brown);
  }
  .write-in {
    position: absolute; left: 304px; width: 252px;
    text-align: right; color: var(--brand-brown); font-size: 15px;
  }
  .write-in--name { top: 42px; }
  .write-in--contact { top: 112px; }
  .write-in__line {
    margin-top: 26px; height: 1px; background: var(--rule);
  }
  .contact-list {
    position: absolute; left: 44px; top: 235px;
    list-style: none; font-size: 16px; line-height: 20px;
  }
  .contact-list li { display: flex; align-items: center; gap: 4px; }
  .contact-list svg { width: 13px; height: 13px; fill: var(--brand-brown); }
  .address {
    position: absolute; right: 34px; top: 235px;
    font-style: normal; text-align: right; font-size: 16px; line-height: 20px;
  }
  .footer-band {
    position: absolute; left: 0; right: 0; bottom: 0; height: 28px;
    color: var(--white); font-size: 16px;
  }
  .footer-band svg { position: absolute; inset: 0; width: 100%; height: 100%; }
  .footer-band__web { position: absolute; left: 44px; top: 3px; }
  .footer-band__license { position: absolute; right: 34px; top: 3px; }
</style>
</head>
<body>
  <section class="card card--front">
    <div class="front-artwork" role="img" aria-label="Photo of dark wooden planks with carpentry tools around the edges: measuring tape, hammer, nails, pliers, wrench, level and drill bit"></div>
    <div class="front-brand">
      <div class="front-brand__name">K&amp;T Fixit and Rebuild</div>
      <div class="front-brand__tagline">General Contractor</div>
    </div>
  </section>

  <section class="card card--back">
    <div class="back-brand">K&amp;T Fixit and Rebuild</div>

    <div class="write-in write-in--name">Name<div class="write-in__line"></div></div>
    <div class="write-in write-in--contact">Contact<div class="write-in__line"></div></div>

    <ul class="contact-list">
      <li><svg viewBox="0 0 24 24" aria-hidden="true"><path d="M6.6 10.8a15 15 0 0 0 6.6 6.6l2.2-2.2c.3-.3.7-.4 1-.2 1.1.4 2.3.6 3.6.6.6 0 1 .4 1 1V20c0 .6-.4 1-1 1A17 17 0 0 1 3 4c0-.6.4-1 1-1h3.5c.6 0 1 .4 1 1 0 1.3.2 2.5.6 3.6.1.3 0 .7-.2 1z"/></svg>360-555-0182</li>
      <li><svg viewBox="0 0 24 24" aria-hidden="true"><path d="M6 2h10v6H6zM3 9h18v9h-3v4H6v-4H3zm5 7v4h8v-4z"/></svg>360-555-0149</li>
      <li><svg viewBox="0 0 24 24" aria-hidden="true"><path d="M2 5h20v14H2zm2 2v.5l8 5 8-5V7zm0 2.8V17h16V9.8l-8 5z"/></svg>office@kandtfixitandrebuild.example</li>
    </ul>

    <address class="address">4417 NE 3rd Ave<br>Ste D246<br>Vancouver, WA 98612</address>

    <div class="footer-band">
      <svg viewBox="0 0 590 28" preserveAspectRatio="none" aria-hidden="true">
        <rect width="590" height="28" fill="var(--band-dark)"/>
        <polygon points="0,0 346,0 330,28 0,28" fill="var(--band-brown)"/>
        <polygon points="346,0 350,0 334,28 330,28" fill="var(--white)"/>
      </svg>
      <span class="footer-band__web">www.kandtfixitandrebuild.example</span>
      <span class="footer-band__license">License #KTFXTRB318QN</span>
    </div>
  </section>
</body>
</html>
```